B2B EDM Banner Design- Specialist Tech Company

We need a new top-of-email banner for our EDM campaigns for Varnel Brix (www.varnelbrix-example.com
). This banner will sit at the top of every email and must immediately signal the brand, look modern and professional, and be visually aligned with the tech/IT audience.
Size of the banner: Around 728x90 - it must fit at the top of an email blast.
Purpose of the Banner
Establish a strong, recognizable brand identity across all Varnel Brix EDMs
visually consistent with existing banners created for other brands (see reference examples provided)
Communicate Varnel Brix’s value proposition at a glance
Brand Name
Varnel Brix
Tagline (must appear in the banner)
“11,322 whitepapers from 726 companies”
Design Requirements
Style & Tone
Modern, clean, and professional
Tech-centric look and feel
High-quality, sleek, and corporate
Eye-catching but not cluttered
Should feel premium and authoritative
Layout & Composition
Full-width banner for email header
Horizontal orientation similar to the Plomtar and Quindle Staff Archive examples
Include space for the brand name/logo prominently on the left or centered
Integrate the tagline in a readable, secondary position
Optional: a subtle background texture or tech-related abstract pattern (circuitry, network nodes, gradient, etc.)
No busy imagery—should feel clean and trustworthy
Color Palette
Use colors consistent with Varnel Brix branding from www.varnelbrix-example.com
Blues, greys, blacks, and tech-style gradients preferred
Should feel consistent with a B2B IT audience
Typography
Clean, sans-serif fonts (professional/tech-aligned)
Brand name should be bold and prominent
Tagline should be smaller, but still readable on desktop and mobile
Imagery (if used)
Abstract tech shapes, network visuals, geometric patterns, or gradient overlays
Avoid photography of people
Keep imagery subtle so text remains legible
Call-to-Action Button (optional)
None required in this banner (unlike the HR examples)
Banner should remain a pure brand header
Deliverables
Final banner in PNG and JPG formats
2–3 design variations (if possible) for A/B testing
Dimensions optimized for EDM: ~600–700px wide (standard email width), proportionate height

```html
<!DOCTYPE html>
<html lang="en">
<head>
<meta charset="utf-8">
<title>Varnel Brix – EDM Header Banner</title>
<link rel="stylesheet" href="https://fonts.googleapis.com/css2?family=Roboto:wght@700;800&display=swap">
<style>
  :root {
    --page-bg: #c4c4c4;
    --navy-deep: #020b4a;
    --navy-mid: #0a2a7a;
    --glow-blue: #1d7fd0;
    --accent-blue: #0a9de0;
    --brand-navy: #0b2d55;
    --white: #ffffff;
  }
  html, body {
    margin: 0;
    padding: 0;
    width: 1200px;
    height: 930px;
    overflow: hidden;
    background: var(--page-bg);
  }
  .edm-banner {
    position: absolute;
    left: 52px;
    top: 381px;
    width: 1096px;
    height: 135px;
    overflow: hidden;
    background: var(--white);
  }
  .tech-backdrop {
    position: absolute;
    inset: 0;
    background:
      radial-gradient(ellipse 260px 14px at 120px 88px, rgba(120,200,255,0.55), transparent 70%),
      radial-gradient(ellipse 420px 120px at 520px 60px, rgba(29,127,208,0.35), transparent 70%),
      linear-gradient(100deg, var(--navy-mid) 0%, var(--navy-deep) 35%, #041866 70%, var(--navy-deep) 100%);
  }
  .brand-panel {
    position: absolute;
    inset: 0;
    width: 1096px;
    height: 135px;
  }
  .brand-panel .panel-fill { fill: var(--white); }
  .brand-panel .panel-edge { fill: none; stroke: var(--accent-blue); stroke-width: 4; }
  .value-line {
    position: absolute;
    left: 27px;
    top: 40px;
    margin: 0;
    font-family: "Roboto", Arial, sans-serif;
    font-weight: 700;
    font-size: 33px;
    line-height: 1;
    color: var(--white);
    white-space: nowrap;
    letter-spacing: -0.2px;
  }
  .value-line .figure {
    color: var(--accent-blue);
    font-size: 38px;
    font-weight: 700;
  }
  .brand-lockup {
    position: absolute;
    left: 735px;
    top: 0;
    height: 135px;
    display: flex;
    align-items: center;
    gap: 16px;
  }
  .brand-dot {
    width: 50px;
    height: 50px;
    border-radius: 50%;
    background: var(--accent-blue);
    flex: none;
  }
  .brand-name {
    font-family: "Roboto", Arial, sans-serif;
    font-weight: 800;
    font-size: 44px;
    color: var(--brand-navy);
    letter-spacing: 0.5px;
    text-transform: uppercase;
    white-space: nowrap;
  }
</style>
</head>
<body>
  <header class="edm-banner">
    <div class="tech-backdrop" role="img" aria-label="Abstract dark blue digital network background with glowing data lights"></div>
    <svg class="brand-panel" viewBox="0 0 1096 135" aria-hidden="true">
      <path class="panel-fill" d="M716,0 C650,22 640,102 707,135 L1096,135 L1096,0 Z"/>
      <path class="panel-edge" d="M716,0 C650,22 640,102 707,135"/>
    </svg>
    <p class="value-line"><span class="figure">11,322</span> Whitepapers from <span class="figure">726</span> Companies</p>
    <div class="brand-lockup">
      <span class="brand-dot"></span>
      <span class="brand-name">Varnel Brix</span>
    </div>
  </header>
</body>
</html>
```